PlumHarbor Coach/Personal trainer needs wordpress site/blog with ecommerce capable membership area

We need a WordPress design for PlumHarborFit.com. This is a blog about wellness, weight loss, and health related topics. Design logo will be provided to the winner.

A great site with a design that we would like to emulate are http://kq4.example. The design should be simple, clean, unique, fun, and distinctive. Above all, it should be highly readable and easy to navigate.

These are the specific sections/categories of the blog that should be included and incorporated into the design SEE BELOW.

Thanks in advance for your consideration
Updates

Reason: I have extended the deadline to evaluate more designs from other pros

Hello all, Please take a minute to review the requirements for this project and please make sure you are capable of meeting ALL the requirements. As you already know I will be making a decision very shortly on whose design I will be moving forward with, if there are any last minute submissions now is the time. Thank you for your time.

Target Market(s)

90 % women 10 % men my clients are usually professionals who value their appearance, health, longevity and time.

Industry/Entity Type

Personal Trainer

Font styles to use
Serif

Colors
886aae
ffcf3e

Requirements
Must have
• Requirements

- start losing weight today.... 555 902 6148 (first line)
- visuals/images and backgrounds to give the idea of wellness, weight loss, healthy living, etc
- navigation menu - home, who we are, what we do, who we serve, blog, contact, members area

1) slider element at top below navigation menu
2) slider element near bottom of page will have testimonials
3) contact form/inquiry form (one page)
4) will provide wellness logo (to give credibility)
5) color scheme purple, gold and white
6) membership area
7) fb, tw, youtube icons
8) footer area - In the footer, there will be smaller company logo, copyright,
disclaimer, privacy policy, terms n conditions, verse of day, and contact info, Phone: (555) 902-6148
Email: support@...
Address:
9) use dummy content/graphic as they will be replaced by real content (the winner will provide instruction on how to make changes to all text and changing graphics)
9) ecommerce enabled / newsletter signup area

```html
<!DOCTYPE html>
<html lang="en">
<head>
<meta charset="utf-8">
<title>PlumHarborFit.com – Your Wellness Starts Today</title>
<link href="https://fonts.googleapis.com/css2?family=Open+Sans:wght@400;600;700&family=Raleway:wght@400;500;600;700&display=swap" rel="stylesheet">
<style>
:root{
  --purple:#6f0fa8;
  --gold:#d9a915;
  --gold-light:#f0c534;
  --green-1:#c7dc7a;
  --green-2:#a9c84a;
  --text:#333;
  --muted:#555;
  --band:#f0f0f0;
  --footer:#3a3a3a;
  --footer-base:#232323;
  --social-1:#3b5998;
  --social-2:#4ab3e8;
  --social-3:#c4302b;
  --social-footer:#6d3fc6;
  --white:#fff;
}
*{box-sizing:border-box;margin:0;padding:0}
html,body{width:671px;height:1200px;overflow:hidden;background:var(--white)}
body{position:relative;font-family:"Open Sans",Arial,sans-serif;color:var(--text)}
.abs{position:absolute}
.top-rule{left:0;top:0;width:671px;height:3px;background:var(--purple)}

/* header */
.social{left:60px;top:32px;display:flex;gap:6px}
.social span{width:20px;height:20px;border-radius:3px;display:block}
.brand{left:256px;top:28px;display:flex;align-items:center;gap:6px}
.brand-mark{width:26px;height:26px;background:var(--gold)}
.brand-name{font-family:"Open Sans",Arial,sans-serif;font-weight:700;font-size:24px;color:var(--purple)}
.callout{left:482px;top:28px}
.callout .tag{font-size:10.5px;color:var(--purple);font-weight:600}
.callout .phone{font-size:13px;font-weight:700;color:#333;letter-spacing:.5px}

/* hero */
.hero{left:0;top:75px;width:671px;height:304px;background:linear-gradient(90deg,var(--green-1),#d4e591 45%,var(--green-2))}
.hero-photo{left:392px;top:104px;width:168px;height:275px;background:linear-gradient(180deg,#f1d9b8,#e8e0d6 45%,#4a4a4a 70%,#cfcfcf);border-radius:60px 60px 0 0;opacity:.9}
.nav{left:55px;top:76px;width:561px;height:22px;background:var(--white);display:flex;align-items:center;justify-content:space-between;padding:0 14px 0 19px;font-family:Arial,sans-serif;font-size:8.2px;letter-spacing:.5px;color:#222}
.nav a{color:#222;text-decoration:none}
.nav .sep{color:#222}
.nav .current{background:var(--gold);color:var(--white);padding:4px 7px}
.hero-title{left:57px;top:192px;font-family:"Open Sans",Arial,sans-serif;color:var(--white);line-height:1}
.hero-title .l1{font-size:35px}
.hero-title .l1 b{font-weight:400;color:var(--purple)}
.hero-title .l2{font-size:24px;margin-top:8px}
.hero-copy{left:58px;top:276px;width:292px;font-family:Arial,sans-serif;font-size:7.7px;line-height:11px;color:var(--white)}

/* welcome */
.welcome-title{left:61px;top:424px;font-family:"Raleway",sans-serif;font-size:18px;color:var(--gold);font-weight:500}
.welcome-title b{font-weight:700}
.welcome-img{left:54px;top:472px;width:128px;height:124px;background:radial-gradient(circle at 45% 45%,#7cc13a 0 35%,#e9e9e9 36% 60%,#fff 61%)}
.welcome-lead{left:194px;top:460px;width:206px;font-size:7.4px;line-height:11px;font-weight:700;color:#222}
.welcome-body{left:194px;top:493px;width:206px;font-size:7.2px;line-height:11.2px;color:var(--muted);text-align:justify}
.ticks{left:188px;top:584px;font-size:7.4px;color:#222}
.ticks li{list-style:none;display:flex;align-items:center;gap:4px;height:20px}

/* appointment */
.booking{left:422px;top:412px;width:192px;height:226px;background:#ececec;border:2px solid #dcdcdc;border-radius:4px}
.booking h2{position:absolute;left:2px;top:2px;width:184px;height:28px;background:var(--purple);color:var(--white);font-family:"Raleway",sans-serif;font-weight:500;font-size:13.5px;padding:4px 0 0 16px}
.field{position:absolute;left:16px;width:158px;height:24px;background:#f7f7f7;border:1px solid #c9c9c9;font-size:7.6px;color:#333;padding:7px 8px}
.field .caret{position:absolute;right:0;top:3px;width:20px;height:16px;border-left:1px solid #ccc}
.booking .submit{position:absolute;left:18px;top:181px;width:156px;height:29px;border-radius:3px;background:linear-gradient(180deg,var(--gold-light),var(--gold));color:var(--white);font-size:11px;text-align:center;line-height:29px}

/* trainers */
.trainers{left:0;top:670px;width:671px;height:207px;background:var(--band)}
.trainers h2{position:absolute;left:0;top:10px;width:671px;text-align:center;font-family:"Raleway",sans-serif;font-weight:700;font-size:22px;color:var(--gold)}
.trainers p{position:absolute;left:150px;top:40px;width:371px;text-align:center;font-size:7.4px;line-height:13px;color:#333}
.card{top:87px;width:171px;height:96px;overflow:hidden}
.card .photo{width:100%;height:100%}
.card .label{position:absolute;left:0;bottom:0;width:100%;height:21px;background:var(--purple);color:var(--white);font-size:13px;padding:1px 0 0 10px}
.card svg{position:absolute;right:0;bottom:0}

/* testimonial */
.portrait{left:70px;top:934px;width:100px;height:100px;border-radius:50%;border:3px solid #e2e2e2;background:linear-gradient(180deg,#dfe6ea,#9aa7b3)}
.client{left:90px;top:1044px;font-size:7.4px;font-weight:700;color:var(--purple)}
.swoosh{left:146px;top:1022px}
.testimonial-title{left:190px;top:930px;font-family:"Raleway",sans-serif;font-weight:700;font-size:18px;color:var(--gold)}
.pager{left:582px;top:929px;display:flex;gap:4px}
.pager span{width:11px;height:10px;display:flex;align-items:center;justify-content:center}
.pager svg{display:block}
.quote-lead{left:193px;top:962px;width:400px;font-size:7.4px;line-height:11px;font-weight:700;color:var(--purple)}
.quote-body{left:193px;top:996px;width:400px;font-size:7.2px;line-height:11.5px;color:#333}

/* footer */
.footer{left:0;top:1070px;width:671px;height:108px;background:var(--footer);color:var(--white)}
.footer h3{position:absolute;top:17px;font-size:8.8px;font-weight:700}
.footer .info{position:absolute;left:66px;top:34px;font-size:7.2px;line-height:11.4px;font-family:Arial,sans-serif}
.footer .res{position:absolute;left:249px;top:34px;font-size:7.2px;line-height:12px}
.footer .res a{color:#b85cff}
.footer .follow{position:absolute;left:249px;top:62px;font-size:9px;font-weight:700}
.footer .icons{position:absolute;left:250px;top:81px;display:flex;gap:5px}
.footer .icons span{width:12px;height:12px;background:var(--social-footer);border-radius:2px;display:block}
.finput{position:absolute;background:var(--white);border:1px solid #bbb;font-size:6px;color:#777;padding:3px 5px}
.fsubmit{position:absolute;left:564px;top:82px;width:48px;height:15px;background:#9b2ee0;color:var(--white);font-size:7.4px;font-weight:700;text-align:center;line-height:15px}
.base{left:0;top:1178px;width:671px;height:22px;background:var(--footer-base);color:var(--white);font-size:6.4px;text-align:center;line-height:22px}
</style>
</head>
<body>
<div class="abs top-rule"></div>

<header>
  <div class="abs social" aria-label="Social profile links">
    <span style="background:var(--social-1)" role="img" aria-label="Social profile link"></span>
    <span style="background:var(--social-2)" role="img" aria-label="Social profile link"></span>
    <span style="background:var(--social-3)" role="img" aria-label="Video channel link"></span>
  </div>
  <div class="abs brand"><span class="brand-mark"></span><span class="brand-name">PlumHarbor</span></div>
  <div class="abs callout">
    <div class="tag">Start losing weight today....</div>
    <div class="phone">555 902 6148</div>
  </div>
</header>

<section class="abs hero" role="img" aria-label="Soft green photo of a bright clinic room"></section>
<div class="abs hero-photo" role="img" aria-label="Photo of a smiling woman eating an apple and holding a bathroom scale"></div>
<nav class="abs nav">
  <a class="current">HOME</a><span class="sep">|</span><a>WHO WE ARE</a><span class="sep">|</span><a>WHAT WE DO</a><span class="sep">|</span><a>WHO WE SERVE</a><span class="sep">|</span><a>CONTACT</a><span class="sep">|</span><a>BLOG</a><span class="sep">|</span><a>MEMBERS</a>
</nav>
<div class="abs hero-title">
  <div class="l1">YOUR <b>WELLNESS</b></div>
  <div class="l2">STARTS TODAY</div>
</div>
<p class="abs hero-copy">Lorem ipsum dolor sit amet, consectetur adipiscing elit, sed do eiusmod tempor incididunt ut labore et dolore magna aliqua but because those who do not know how to encounter consequences..</p>

<section>
  <h1 class="abs welcome-title">WELCOME TO <b>PLUMHARBOR</b></h1>
  <div class="abs welcome-img" role="img" aria-label="Photo of a green apple wrapped in a tape measure"></div>
  <p class="abs welcome-lead">Lorem ipsum dolor sit amet, consectetur adipiscing elit, sed do eiusmod tempor incididunt</p>
  <p class="abs welcome-body">ut labore et dolore magna aliqua. Ut enim ad minim veniam, quis nostrud exercitation ullamco laboris nisi ut aliquip ex ea commodo consequat. Sed ut perspiciatis unde omnis iste natus error sit voluptatem accusantium doloremque laudantium, totam rem aperiam, eaque ipsa quae ab illo inventore veritatis et quasi architecto beatae vitae dicta sunt explicabo.</p>
  <ul class="abs ticks">
    <li><svg width="10" height="10" viewBox="0 0 10 10"><path d="M1 5l3 3 5-7" fill="none" stroke="#6f0fa8" stroke-width="1.6"/></svg>Contrary to popular belief,</li>
    <li><svg width="10" height="10" viewBox="0 0 10 10"><path d="M1 5l3 3 5-7" fill="none" stroke="#6f0fa8" stroke-width="1.6"/></svg>Lorem ipsum dolor sit amet,</li>
  </ul>

  <form class="abs booking">
    <h2>Book an Appointment</h2>
    <div class="field" style="top:44px">Select Department<span class="caret"></span></div>
    <div class="field" style="top:78px">Your Full Name(Required)</div>
    <div class="field" style="top:112px">Your Email</div>
    <div class="field" style="top:146px">Date Of A Appoinment</div>
    <div class="submit">SUBMIT</div>
  </form>
</section>

<section class="abs trainers">
  <h2>OUR TRAINERS</h2>
  <p>Lorem ipsum dolor sit amet, consectetur adipiscing elit. Cras vitae odio id sapien tempus elementum. Cras vitae odio id sapien tempus elementum.</p>
  <div class="abs card" style="left:55px">
    <div class="photo" role="img" aria-label="Photo of a trainer stretching a client's leg in a gym" style="background:linear-gradient(135deg,#8d9298,#c9c4bd)"></div>
    <div class="label">Weight Loss</div>
    <svg width="70" height="60" viewBox="0 0 70 60"><polygon points="70,0 70,60 0,60" fill="#000"/><text x="44" y="50" fill="#fff" font-size="11" font-family="Open Sans,sans-serif" transform="rotate(-45 44 50)">INFO</text></svg>
  </div>
  <div class="abs card" style="left:250px">
    <div class="photo" role="img" aria-label="Photo of a woman receiving a back massage" style="background:linear-gradient(135deg,#f3f1ef,#d6a88a)"></div>
    <div class="label">Fitness</div>
    <svg width="70" height="60" viewBox="0 0 70 60"><polygon points="70,0 70,60 0,60" fill="#000"/><text x="44" y="50" fill="#fff" font-size="11" font-family="Open Sans,sans-serif" transform="rotate(-45 44 50)">INFO</text></svg>
  </div>
  <div class="abs card" style="left:444px">
    <div class="photo" role="img" aria-label="Photo of a man working out on a gym bench with a coach" style="background:linear-gradient(135deg,#e6e6e6,#8e8e8e)"></div>
    <div class="label">Fitness</div>
    <svg width="70" height="60" viewBox="0 0 70 60"><polygon points="70,0 70,60 0,60" fill="#000"/><text x="44" y="50" fill="#fff" font-size="11" font-family="Open Sans,sans-serif" transform="rotate(-45 44 50)">INFO</text></svg>
  </div>
</section>

<section>
  <div class="abs portrait" role="img" aria-label="Portrait photo of a client"></div>
  <svg class="abs swoosh" width="54" height="30" viewBox="0 0 54 30"><path d="M2 26c20 4 36-4 46-20" fill="none" stroke="#bbb" stroke-width="2"/><path d="M40 6l9-1-2 9" fill="none" stroke="#bbb" stroke-width="2"/></svg>
  <div class="abs client">Mr Alan Brook...</div>
  <h2 class="abs testimonial-title">TESTIMONIAL</h2>
  <div class="abs pager">
    <span style="background:#ccc"><svg width="6" height="8" viewBox="0 0 6 8"><path d="M5 1L1 4l4 3" fill="none" stroke="#666"/></svg></span>
    <span style="background:#111"><svg width="6" height="8" viewBox="0 0 6 8"><path d="M1 1l4 3-4 3" fill="none" stroke="#fff"/></svg></span>
  </div>
  <p class="abs quote-lead">Lorem ipsum dolor sit amet, consectetur adipiscing elit, sed do eiusmod tempor incididunt ut labore et dolore magna aliqua.</p>
  <p class="abs quote-body">Ut enim ad minim veniam, quis nostrud exercitation ullamco laboris nisi ut aliquip ex ea commodo consequat. Duis aute irure dolor in reprehenderit in voluptate velit esse cillum.</p>
</section>

<footer class="abs footer">
  <h3 style="left:65px">CONTACT US TODAY</h3>
  <div class="info">TOLL-FREE: (555) 318-2290<br>418 Harbor Way, dummy content/graphic, Ste 102<br>Bayview, FL 33999<br>Local number: 1-555-410-7732<br>Fax number: 1-555-410-7790</div>
  <h3 style="left:249px">RESOURCES</h3>
  <div class="res">Medical Website Design<br><a>support@plumharborfit.example</a></div>
  <div class="follow">Follow us on</div>
  <div class="icons" aria-label="Social profile links"><span></span><span></span><span></span><span></span><span></span></div>
  <h3 style="left:407px">CONTACT FORM</h3>
  <div class="finput" style="left:409px;top:38px;width:88px;height:14px">Name</div>
  <div class="finput" style="left:409px;top:59px;width:88px;height:15px">E-Mail</div>
  <div class="finput" style="left:508px;top:38px;width:104px;height:36px">Message</div>
  <div class="fsubmit">Submit</div>
</footer>
<div class="abs base">Copyright © 2014 PlumHarbor Fit. All rights reserved.</div>
</body>
</html>
```